need illustration for a landing page

creating a landing page for a launch meme coin. I need illustrations for a landing page
similar to https://brindlemint.io/ but featuring the cat and cat themed. must be a bit more serious than the chicken. check out zavolet.com

```html
<!DOCTYPE html>
<html lang="en">
<head>
<meta charset="utf-8">
<title>Zavolet – Join the Revolution</title>
<link rel="stylesheet" href="https://fonts.googleapis.com/css2?family=Outfit:wght@300;400;600;700&display=swap">
<style>
  :root {
    --night: #03042a;
    --night-deep: #02021c;
    --panel: rgba(22, 28, 70, 0.38);
    --orange: #e2410f;
    --blue: #1366ff;
    --white: #ffffff;
    --moon-tone: rgba(255, 210, 0, 0.85);
    --cyan-tone: rgba(31, 214, 255, 0.45);
    --ember-tone: rgba(255, 96, 20, 0.5);
  }
  * { margin: 0; padding: 0; box-sizing: border-box; }
  html, body { width: 1200px; height: 560px; overflow: hidden; background: var(--night); }
  .hero {
    position: relative;
    width: 1200px;
    height: 560px;
    overflow: hidden;
    font-family: "Outfit", sans-serif;
    color: var(--white);
    background: var(--night);
  }
  .night-scene {
    position: absolute;
    inset: 0;
    background:
      radial-gradient(circle at 10px 40px, var(--moon-tone) 0, rgba(255,210,0,0) 140px),
      radial-gradient(circle at 580px 545px, var(--ember-tone) 0, rgba(255,96,20,0) 120px),
      radial-gradient(circle at 1180px 400px, var(--ember-tone) 0, rgba(255,96,20,0) 110px),
      radial-gradient(circle at 1090px 350px, var(--cyan-tone) 0, rgba(31,214,255,0) 120px),
      radial-gradient(circle at 0 560px, var(--cyan-tone) 0, rgba(31,214,255,0) 140px),
      radial-gradient(ellipse at 900px 100px, rgba(30,120,180,0.35) 0, rgba(30,120,180,0) 320px),
      linear-gradient(180deg, var(--night-deep) 0%, var(--night) 60%, #0d1040 100%);
  }
  .mascot-art {
    position: absolute;
    left: 123px; top: 58px;
    width: 332px; height: 447px;
    border-radius: 24px;
    background:
      radial-gradient(ellipse at 50% 15%, rgba(240,190,40,0.35) 0, rgba(240,190,40,0) 90px),
      linear-gradient(90deg, rgba(210,55,10,0.35) 0%, rgba(40,30,90,0.25) 50%, rgba(20,100,255,0.4) 100%);
  }
  .panel {
    position: absolute;
    left: 507px; top: 58px;
    width: 449px; height: 445px;
    border-radius: 18px;
    background: var(--panel);
  }
  .headline {
    position: absolute;
    left: 538px; top: 104px;
    font-weight: 700;
    font-size: 41.5px;
    line-height: 40px;
    letter-spacing: -0.5px;
  }
  .headline .line-warm { color: var(--orange); display: block; }
  .headline .line-cool { color: var(--blue); display: block; }
  .tagline {
    position: absolute;
    left: 537px; top: 205px;
    font-weight: 600;
    font-size: 16px;
    letter-spacing: -0.2px;
    white-space: nowrap;
  }
  .intro {
    position: absolute;
    left: 538px; top: 245px;
    width: 392px;
    font-weight: 300;
    font-size: 16.6px;
    line-height: 23px;
  }
  .cta {
    position: absolute;
    left: 542px; top: 425px;
    width: 218px; height: 43px;
    border: 2px solid var(--blue);
    display: flex; align-items: center; justify-content: center;
    font-weight: 700;
    font-size: 21px;
    letter-spacing: 1px;
    color: var(--white);
    text-decoration: none;
  }
</style>
</head>
<body>
<main class="hero">
  <div class="night-scene" role="img" aria-label="Night sky scene with a full moon, scattered stars, drifting clouds, a small glowing pagoda house and a winding path"></div>
  <div class="mascot-art" role="img" aria-label="Line-art illustration of a crowned cat head in red and blue"></div>

  <section class="panel" aria-hidden="true"></section>
  <h1 class="headline"><span class="line-warm">JOIN THE</span><span class="line-cool">REVOLUTION</span></h1>
  <p class="tagline">Zavolet (ZAVL$): The Future of Feline Finance</p>
  <p class="intro">Zavolet (ZAVL$) is a meme-driven cryptocurrency with claws. Inspired by the resilience and independence of cat lovers everywhere, Zavolet is more than just a joke—it’s a movement. Built on a foundation of humor, social commentary, and financial empowerment, Zavolet takes on the world with the cunning of a cat queen.</p>
  <a class="cta" href="#">GET STARTED</a>
</main>
</body>
</html>
```